DEAN COLLOPY PROPERTY SERVICES

I want a business card that is clean and simple.
'Dean Collopy Property Services' is the title.
Somewhere on the card needs to be 'Carpentry, Tiling, painting and garden services'

On the back of card
PH 087 394 1526
email: deancollopypropertyservices@bluefinchmail.net

I have attached a picture of my other business. I would like the font and design to be similar to the bathroom business.

Many thanks.

```html
<!DOCTYPE html>
<html lang="en">
<head>
<meta charset="utf-8">
<title>Dean Collopy Property Services – Business Card</title>
<link href="https://fonts.googleapis.com/css2?family=Montserrat:wght@500;600&family=Roboto:wght@400;500&display=swap" rel="stylesheet">
<style>
  :root {
    --backdrop: #262626;
    --card: #0d0d0d;
    --card-edge: #1a1a1a;
    --ink: #ffffff;
    --ink-soft: #d9d9d9;
    --rule: #555555;
  }
  * { margin: 0; padding: 0; box-sizing: border-box; }
  html, body {
    width: 1200px;
    height: 900px;
    overflow: hidden;
    background: var(--backdrop);
  }
  .canvas {
    position: relative;
    width: 1200px;
    height: 900px;
    background: radial-gradient(ellipse at 50% 45%, #2e2e2e 0%, var(--backdrop) 70%);
  }
  .card {
    position: absolute;
    top: 295px;
    width: 540px;
    height: 310px;
    background: var(--card);
    border: 1px solid var(--card-edge);
    box-shadow: 0 12px 30px rgba(0,0,0,0.55);
    color: var(--ink);
  }
  .card--contact { left: 40px; }
  .card--brand { left: 620px; }

  .wordmark {
    position: absolute;
    text-align: right;
    font-family: "Montserrat", sans-serif;
    font-weight: 600;
    color: var(--ink);
    line-height: 1;
  }
  .wordmark__name { display: block; font-size: 40px; letter-spacing: 0.5px; }
  .wordmark__sub {
    display: block;
    margin-top: 8px;
    font-size: 13px;
    letter-spacing: 4.2px;
  }
  .card--contact .wordmark { top: 70px; right: 50px; }
  .card--brand .wordmark { top: 95px; left: 0; right: 0; text-align: center; }

  .divider-top {
    position: absolute;
    top: 158px;
    right: 0;
    width: 230px;
    height: 1px;
    background: var(--rule);
  }
  .person {
    position: absolute;
    left: 40px;
    top: 188px;
    font-family: "Roboto", sans-serif;
  }
  .person__name {
    font-family: "Montserrat", sans-serif;
    font-weight: 600;
    font-size: 22px;
    letter-spacing: 0.5px;
  }
  .person__role {
    display: flex;
    align-items: center;
    gap: 10px;
    font-size: 14px;
    color: var(--ink-soft);
    margin-top: 2px;
  }
  .person__rule { width: 170px; height: 1px; background: var(--rule); }
  .contact {
    position: absolute;
    left: 40px;
    top: 250px;
    font-family: "Roboto", sans-serif;
    font-size: 14px;
    color: var(--ink-soft);
    list-style: none;
  }
  .contact li { display: flex; align-items: center; gap: 8px; line-height: 22px; }
  .contact svg { width: 14px; height: 14px; fill: var(--ink-soft); }

  .services {
    position: absolute;
    top: 205px;
    left: 0;
    right: 0;
    text-align: center;
    font-family: "Roboto", sans-serif;
    font-size: 15px;
    color: var(--ink-soft);
  }
  .services .dot { margin: 0 6px; }
</style>
</head>
<body>
<main class="canvas">

  <section class="card card--contact">
    <div class="wordmark">
      <span class="wordmark__name">Dean Collopy</span>
      <span class="wordmark__sub">PROPERTY SERVICES</span>
    </div>
    <div class="divider-top"></div>

    <div class="person">
      <p class="person__name">RONAN KEANE</p>
      <p class="person__role">Managing Director <span class="person__rule"></span></p>
    </div>

    <ul class="contact">
      <li>
        <svg viewBox="0 0 24 24" aria-hidden="true"><path d="M6.6 10.8a15.1 15.1 0 0 0 6.6 6.6l2.2-2.2a1 1 0 0 1 1-.25 11.4 11.4 0 0 0 3.6.57 1 1 0 0 1 1 1V20a1 1 0 0 1-1 1A17 17 0 0 1 3 4a1 1 0 0 1 1-1h3.5a1 1 0 0 1 1 1c0 1.25.2 2.45.57 3.57a1 1 0 0 1-.25 1z"/></svg>
        087 394 1526
      </li>
      <li>
        <svg viewBox="0 0 24 24" aria-hidden="true"><path d="M2 5h20v14H2z M4 7v.5l8 5.5 8-5.5V7l-8 5.5z" fill-rule="evenodd"/></svg>
        deancollopypropertyservices@bluefinchmail.net
      </li>
    </ul>
  </section>

  <section class="card card--brand">
    <div class="wordmark">
      <span class="wordmark__name">Dean Collopy</span>
      <span class="wordmark__sub">PROPERTY SERVICES</span>
    </div>
    <p class="services">
      Carpentry<span class="dot">•</span>Tiling<span class="dot">•</span>Painting<span class="dot">•</span>Garden Services
    </p>
  </section>

</main>
</body>
</html>
```